Business Card Design for a Design/Build Firm

Harrowgate Structures Group, Inc. is a firm providing construction professional project management and architectural design services to an international clientele. Contemporary. "Green" movement aware. Business card to have back design/logo. Cards will be on high gloss paper

Target Market(s)

Building Developers and Owners

Industry/Entity Type

Construction

Requirements
Nice to have
• We really would like to use the acronym "HSG" as main focal point fo card design. Company will be known as HSG.
Should not have
• No globes or abstract images of buildings.

```html
<!DOCTYPE html>
<html lang="en">
<head>
<meta charset="utf-8">
<title>Harrowgate Structures Group – Business Card</title>
<link rel="stylesheet" href="https://fonts.googleapis.com/css2?family=Questrial&family=Roboto+Condensed:wght@400&display=swap">
<style>
  :root {
    --canvas-bg: #dfe4e7;
    --brand-blue: #2f6fbd;
    --brand-blue-deep: #2b559a;
    --brand-blue-bright: #2a93d3;
    --pale-blue: #bcd1e7;
    --ink: #1d1d1d;
    --grey: #6b6b6b;
    --rule: #8a8a8a;
    --white: #ffffff;
  }
  * { box-sizing: border-box; margin: 0; padding: 0; }
  html, body {
    width: 1200px; height: 960px; overflow: hidden;
    background: var(--canvas-bg);
  }
  .canvas {
    width: 1200px; height: 960px;
    display: flex; flex-direction: column; align-items: center; justify-content: center;
    gap: 40px;
  }
  .card {
    position: relative; width: 735px; height: 420px; overflow: hidden;
    box-shadow: 0 6px 20px rgba(0,0,0,.18);
  }

  /* Front */
  .card-front {
    background: radial-gradient(ellipse at 45% 45%, #ffffff 0%, #f6f6f6 60%, #ececec 100%);
  }
  .brand-lockup {
    position: absolute; top: 28px; right: 26px;
    display: flex; align-items: center; gap: 10px;
  }
  .brand-dot {
    width: 46px; height: 46px; border-radius: 50%; background: var(--brand-blue);
  }
  .brand-divider { width: 1px; height: 50px; background: var(--rule); }
  .brand-name {
    font-family: "Questrial", sans-serif; font-size: 14px; color: var(--brand-blue);
  }
  .person {
    position: absolute; top: 80px; left: 86px; text-align: right;
  }
  .person-name {
    font-family: "Questrial", sans-serif; font-size: 42px; color: var(--brand-blue);
    line-height: 1;
  }
  .person-title {
    font-family: "Questrial", sans-serif; font-size: 24px; color: var(--grey);
    margin-top: 4px;
  }
  .monogram-circle {
    position: absolute; left: 10px; top: 220px;
    width: 330px; height: 330px; border-radius: 50%; background: var(--pale-blue);
  }
  .monogram-text {
    position: absolute; left: 30px; top: 268px;
    font-family: "Questrial", sans-serif; font-size: 170px; line-height: 1;
    color: var(--white); letter-spacing: -4px;
  }
  .contact-rule {
    position: absolute; left: 385px; top: 235px; width: 3px; height: 215px;
    background: var(--rule);
  }
  .contact-list {
    position: absolute; left: 425px; top: 250px; list-style: none;
    font-family: "Roboto Condensed", sans-serif; font-size: 17px; color: var(--ink);
    line-height: 1.3;
  }
  .contact-list li { display: flex; align-items: flex-start; gap: 10px; }
  .contact-list svg { flex: 0 0 16px; margin-top: 3px; }
  .contact-list .indent { padding-left: 26px; }

  /* Back */
  .card-back {
    background: radial-gradient(ellipse at 40% 50%, var(--brand-blue-bright) 0%, #2878bf 45%, var(--brand-blue-deep) 100%);
  }
  .back-mark {
    position: absolute; left: 50%; top: 52px; transform: translateX(-50%);
    width: 86px; height: 86px; border-radius: 50%; background: var(--white);
  }
  .back-name {
    position: absolute; top: 158px; width: 100%; text-align: center;
    font-family: "Questrial", sans-serif; font-size: 26px; letter-spacing: 2px;
    color: var(--white);
  }
  .back-circle {
    position: absolute; right: -60px; top: 215px;
    width: 340px; height: 340px; border-radius: 50%; background: rgba(255,255,255,.25);
  }
  .back-monogram {
    position: absolute; right: -8px; top: 260px;
    font-family: "Questrial", sans-serif; font-size: 130px; line-height: 1;
    color: var(--brand-blue-deep); letter-spacing: -2px;
  }
</style>
</head>
<body>
<main class="canvas">

  <section class="card card-front">
    <div class="brand-lockup">
      <span class="brand-dot"></span>
      <span class="brand-divider"></span>
      <span class="brand-name">Harrowgate Structures Group, Inc.</span>
    </div>

    <div class="person">
      <p class="person-name">Daniel Orwell</p>
      <p class="person-title">Director</p>
    </div>

    <div class="monogram-circle"></div>
    <p class="monogram-text">HSG</p>

    <div class="contact-rule"></div>
    <ul class="contact-list">
      <li>
        <svg width="16" height="16" viewBox="0 0 16 16"><path d="M8 1 L15 8 H13 V15 H10 V10 H6 V15 H3 V8 H1 Z" fill="var(--brand-blue)"/></svg>
        <span>48 Alder Lane, Suite 5</span>
      </li>
      <li class="indent">NV 214</li>
      <li>
        <svg width="16" height="16" viewBox="0 0 16 16"><path d="M4 1 C2 2 2 5 4 9 C6 13 9 15 11 15 L13 13 L10 10 L8.5 11 C7 10 6 8 5.5 6.5 L7 5 L5 1 Z" fill="var(--brand-blue)"/></svg>
        <span>000-0000-000</span>
      </li>
      <li>
        <svg width="16" height="16" viewBox="0 0 16 16"><rect x="1.5" y="3.5" width="13" height="9" fill="none" stroke="var(--brand-blue)" stroke-width="1.5"/><path d="M1.5 3.5 L8 9 L14.5 3.5" fill="none" stroke="var(--brand-blue)" stroke-width="1.5"/></svg>
        <span>info@harrowgatesg.com</span>
      </li>
      <li>
        <svg width="16" height="16" viewBox="0 0 16 16"><circle cx="8" cy="8" r="7" fill="var(--brand-blue)"/></svg>
        <span>www.harrowgatesg.com</span>
      </li>
      <li>
        <svg width="16" height="16" viewBox="0 0 16 16"><rect x="1" y="1" width="14" height="14" rx="2" fill="var(--brand-blue)"/></svg>
        <span>@ HSG</span>
      </li>
    </ul>
  </section>

  <section class="card card-back">
    <span class="back-mark"></span>
    <p class="back-name">Harrowgate Structures Group, Inc.</p>
    <div class="back-circle"></div>
    <p class="back-monogram">HSG</p>
  </section>

</main>
</body>
</html>
```